Website redesign - vornatic.com

We are looking to do a full redesign of vornatic.com. Need a designer to come up overall layout and 3 specific pages and 3 different hero images.
Wireframes for the 3 pages are attached as well as site images. You don't have to follow the wireframes exactly, but instead the wireframe is there to show you the information that needs to be on each page. Feel free to rearrange as needed.
Our target market is self taught engineers. So definitely I want a more casual feel to it. I'm ok with fun bold colors as well. Really like websites that have the infinite scroll look/feel to them.
Looking to find a designer who will produce HTML and potentially even implement the HTML into our site checked in code.
HTML Code should be responsive/mobile first leveraging Bootstrap 4.
Attached files include:
0) Wireframe PDF
https://files.plexarbox.net/file/d/48K-7bQwTn3peRkW21xLmsZfYdgaCb/view?usp=sharing
1) Vornatic Images zip 1
https://files.plexarbox.net/file/d/48m5KZqT29Wr7sHyPbnDuwXcgEjsLF/view?usp=sharing
2) Vornatic Images zip 2
https://files.plexarbox.net/file/d/48uvd3MfTQ2nXbKpJaYeHsCwzLdGHN/view?usp=sharing
Target Market(s)
I sell DIY Waterproof Electronics enclosures. Target audience is self taught DIY engineers
Coding
Coded - Design and coding required
Number of Pages Required
3 page
Colors
Designer to choose colors to be used in the design.
Look and feel
Each slider illustrates characteristics of the customer's brand and the style your logo design should communicate.

```html
<!DOCTYPE html>
<html lang="en">
<head>
<meta charset="utf-8">
<title>Vornatic – Waterproof Project Boxes</title>
<link rel="stylesheet" href="https://fonts.googleapis.com/css2?family=Poppins:ital,wght@0,300;0,400;0,500;0,600;0,700;1,400&display=swap">
<style>
:root{
  --blue:#0a1ff2;
  --yellow:#e6b80b;
  --ink:#3a3d45;
  --muted:#8b8f98;
  --grey-band:#e6e9ee;
  --panel:#f4f5f8;
  --footer:#404753;
  --white:#ffffff;
  --kit-dark:#3e4146;
  --kit-mid:#8d9096;
  --kit-green:#5e8a55;
}
*{margin:0;padding:0;box-sizing:border-box}
html,body{width:1200px;height:3150px;overflow:hidden;background:var(--white)}
body{position:relative;font-family:'Poppins',sans-serif;color:var(--ink)}
.abs{position:absolute}
.btn{position:absolute;display:flex;align-items:center;justify-content:center;height:35px;width:135px;border-radius:18px;background:var(--yellow);color:#222;font-size:12px;font-weight:500;text-decoration:none}

/* header */
.site-header{position:absolute;left:0;top:0;width:1200px;height:75px;background:var(--white)}
.brand{position:absolute;left:120px;top:18px;font-size:30px;font-weight:600;color:var(--blue);letter-spacing:.5px;display:flex;align-items:center;gap:8px}
.brand-dot{width:12px;height:12px;border-radius:50%;background:var(--yellow)}
.main-nav{position:absolute;left:455px;top:29px;display:flex;gap:31px;font-size:12px}
.main-nav a{color:var(--ink);text-decoration:none}
.main-nav a.active{color:var(--blue)}
.btn-login,.btn-signup{position:absolute;top:20px;height:36px;border-radius:18px;display:flex;align-items:center;justify-content:center;font-size:12px;text-decoration:none}
.btn-login{left:886px;width:90px;border:1px solid var(--blue);color:var(--blue)}
.btn-signup{left:990px;width:90px;background:var(--blue);color:var(--white);font-weight:500}

/* hero */
.hero-photo{position:absolute;left:0;top:75px}
.hero-title{position:absolute;left:0;top:258px;width:1200px;text-align:center;color:var(--white);font-size:38px;font-weight:700;line-height:43px}
.hero-arrow{position:absolute;top:324px}

/* feature rows */
.photo{position:absolute;box-shadow:0 18px 30px rgba(0,0,0,.12)}
.feature-title{position:absolute;font-size:23px;font-weight:300;line-height:30px;color:var(--ink)}
.feature-list{position:absolute;left:645px;top:1657px;list-style:none;font-size:14px;font-weight:300;line-height:22.5px;color:var(--muted);width:370px}
.feature-list li{position:relative;padding-left:24px}
.feature-list li::before{content:"•";position:absolute;left:0}

/* testimonials */
.reviews-title{position:absolute;left:0;top:2018px;width:1200px;text-align:center;color:var(--white);font-size:22px;font-weight:600}
.quote-box{position:absolute;top:2078px;width:447px;height:112px;border:1px solid rgba(255,255,255,.75);padding:22px 62px 0 30px;color:var(--white);font-size:14px;font-style:italic;line-height:21px}
.quote-mark{position:absolute;top:2100px;width:24px;height:18px;background:var(--blue)}
.quote-author{position:absolute;top:2201px;color:var(--white);font-size:11px;font-weight:600}
.dots{position:absolute;left:570px;top:2252px;display:flex;gap:6px}
.dots span{width:11px;height:11px;border-radius:50%;border:1px solid var(--white)}
.dots span.on{background:radial-gradient(circle,var(--white) 2px,transparent 2.5px)}

/* examples */
.examples-title{position:absolute;left:0;top:2408px;width:1200px;text-align:center;font-size:23px;font-weight:500;color:#3b3e46}
.example{position:absolute;width:218px}
.example-img{width:218px;height:218px;background:
  radial-gradient(ellipse 42% 26% at 50% 56%,var(--kit-dark) 0%,var(--kit-mid) 55%,rgba(244,245,248,0) 100%),
  radial-gradient(ellipse 30% 16% at 50% 42%,rgba(94,138,85,.55) 0%,rgba(94,138,85,0) 100%),
  var(--panel)}
.example-img.light{background:
  radial-gradient(ellipse 45% 30% at 50% 50%,#9fa6a0 0%,#c6cbc9 55%,rgba(244,245,248,0) 100%),
  radial-gradient(ellipse 30% 16% at 45% 45%,rgba(94,138,85,.5) 0%,rgba(94,138,85,0) 100%),
  #eceef1}
.example-img.psu{background:
  radial-gradient(ellipse 40% 18% at 50% 38%,#c9ccd1 0%,rgba(201,204,209,0) 100%),
  radial-gradient(ellipse 42% 26% at 50% 58%,var(--kit-dark) 0%,var(--kit-mid) 55%,rgba(244,245,248,0) 100%),
  var(--panel)}
.example-name{font-size:13px;color:var(--ink);margin-top:18px;line-height:16px}
.example-sub{font-size:11px;color:var(--muted);line-height:16px}
.example.current .example-name{color:var(--blue);margin-top:21px}

/* footer */
.site-footer{position:absolute;left:0;top:3095px;width:1200px;height:55px;background:var(--footer);color:var(--white)}
.copyright{position:absolute;left:120px;top:20px;font-size:11px}
.follow{position:absolute;left:929px;top:20px;font-size:10px}
.social{position:absolute;top:10px;width:34px;height:34px;border-radius:50%;background:#8a909b}
</style>
</head>
<body>

<header class="site-header">
  <div class="brand">vornatic<span class="brand-dot"></span></div>
  <nav class="main-nav">
    <a class="active" href="#">Get Started</a>
    <a href="#">Designs</a>
    <a href="#">FAQs</a>
    <a href="#">Videos</a>
    <a href="#">Contact Us</a>
  </nav>
  <a class="btn-login" href="#">Login</a>
  <a class="btn-signup" href="#">Sign Up</a>
</header>

<!-- hero -->
<svg class="hero-photo" width="1200" height="526" viewBox="0 0 1200 526" role="img" aria-label="Project box kit parts, printed instructions, screwdriver and pliers laid out on a plywood workbench">
  <defs>
    <linearGradient id="wood" x1="0" y1="0" x2="1" y2="1">
      <stop offset="0" stop-color="#b07a45"/>
      <stop offset="0.5" stop-color="#9a6a3c"/>
      <stop offset="1" stop-color="#b5814e"/>
    </linearGradient>
  </defs>
  <polygon points="0,0 1200,0 1200,525 0,450" fill="url(#wood)"/>
</svg>
<h1 class="hero-title">Waterproof Project Box assembled<br>in half the time</h1>
<a class="btn" href="#" style="left:532px;top:369px">Get Started</a>
<svg class="hero-arrow" style="left:45px" width="30" height="30" viewBox="0 0 30 30"><circle cx="15" cy="15" r="13" fill="none" stroke="#fff" stroke-width="2"/><path d="M17 9 L11 15 L17 21" fill="none" stroke="#fff" stroke-width="2"/></svg>
<svg class="hero-arrow" style="left:1125px" width="30" height="30" viewBox="0 0 30 30"><circle cx="15" cy="15" r="13" fill="none" stroke="#fff" stroke-width="2"/><path d="M13 9 L19 15 L13 21" fill="none" stroke="#fff" stroke-width="2"/></svg>

<!-- designer feature -->
<svg class="photo" style="left:120px;top:638px" width="465" height="300" viewBox="0 0 465 300" role="img" aria-label="Video of a power supply and green controller board mounted inside a project box">
  <defs>
    <linearGradient id="board" x1="0" y1="0" x2="1" y2="0">
      <stop offset="0" stop-color="#8e9096"/>
      <stop offset="0.45" stop-color="#6d7075"/>
      <stop offset="0.55" stop-color="#2f6b3d"/>
      <stop offset="1" stop-color="#3d7a3c"/>
    </linearGradient>
  </defs>
  <rect width="465" height="300" fill="url(#board)"/>
  <circle cx="232" cy="150" r="19" fill="none" stroke="#fff" stroke-width="3"/>
  <path d="M226 140 L242 150 L226 160 Z" fill="none" stroke="#fff" stroke-width="3" stroke-linejoin="round"/>
</svg>
<h2 class="feature-title" style="left:645px;top:732px">Customize your Project Box<br>using our Designer</h2>
<a class="btn" href="#" style="left:645px;top:817px">Get Started</a>

<!-- mounting kits band -->
<svg class="abs" style="left:0;top:975px" width="1200" height="525" viewBox="0 0 1200 525">
  <polygon points="0,75 1200,0 1200,525 0,450" fill="var(--grey-band)"/>
  <polygon points="450,114 495,132 495,364 450,412" fill="var(--panel)"/>
  <polygon points="495,114 540,132 540,364 495,412" fill="#eceef2"/>
  <polygon points="540,114 614,144 614,364 540,412" fill="var(--panel)"/>
  <rect x="614" y="114" width="302" height="298" fill="#fff"/>
  <polygon points="916,144 990,114 990,412 916,364" fill="var(--panel)"/>
  <polygon points="990,132 1035,114 1035,412 990,364" fill="#fff"/>
  <polygon points="1035,132 1080,114 1080,412 1035,364" fill="var(--panel)"/>
</svg>
<h2 class="feature-title" style="left:120px;top:1152px">Mounting Kits for all the<br>popular water proof<br>project boxes with many<br>sizes to choose from</h2>
<a class="btn" href="#" style="left:120px;top:1297px">Get Started</a>

<!-- makers feature -->
<svg class="photo" style="left:120px;top:1538px" width="465" height="337" viewBox="0 0 465 337" role="img" aria-label="Cut mounting plate with controller boards, power supply and bagged hardware on a plywood bench">
  <defs>
    <linearGradient id="plate" x1="0" y1="0" x2="1" y2="1">
      <stop offset="0" stop-color="#a87a4c"/>
      <stop offset="0.5" stop-color="#c8a27a"/>
      <stop offset="1" stop-color="#b68a5d"/>
    </linearGradient>
  </defs>
  <rect width="465" height="337" fill="url(#plate)"/>
</svg>
<h2 class="feature-title" style="left:645px;top:1587px">Vornatic waterproof project boxes<br>were built by makers for makers</h2>
<ul class="feature-list">
  <li>Design to your specifications</li>
  <li>Maker components: Kestrel, Bramble Board,<br>Voltmere Power</li>
  <li>Detailed build instructions, videos, walkthroughs</li>
  <li>DIY made to look professional</li>
</ul>
<a class="btn" href="#" style="left:645px;top:1800px">Get Started</a>

<!-- testimonials -->
<svg class="abs" style="left:0;top:1913px" width="1200" height="465" viewBox="0 0 1200 465">
  <polygon points="0,75 1200,0 1200,465 0,390" fill="var(--blue)"/>
  <polyline points="198,277 178,307 178,277" fill="var(--blue)" stroke="rgba(255,255,255,.75)" stroke-width="1"/>
  <polyline points="693,277 673,307 673,277" fill="var(--blue)" stroke="rgba(255,255,255,.75)" stroke-width="1"/>
</svg>
<h2 class="reviews-title">What our Customers Have to Say?</h2>
<div class="quote-box" style="left:138px">Great work at a reasonable cost. I can't recommend them enough. If you're doing custom boxes for light shows, this is where you go.</div>
<div class="quote-box" style="left:633px">Fantastic service/product... whether you simply generate the design and do all of the fabrication yourself or simply order the kits</div>
<svg class="quote-mark" style="left:126px" viewBox="0 0 24 18" aria-hidden="true">
  <g fill="none" stroke="#fff" stroke-width="2" stroke-linecap="round">
    <circle cx="5.5" cy="12" r="3.8"/><path d="M2 11 Q3 5 8 2"/>
    <circle cx="17.5" cy="12" r="3.8"/><path d="M14 11 Q15 5 20 2"/>
  </g>
</svg>
<svg class="quote-mark" style="left:621px" viewBox="0 0 24 18" aria-hidden="true">
  <g fill="none" stroke="#fff" stroke-width="2" stroke-linecap="round">
    <circle cx="5.5" cy="12" r="3.8"/><path d="M2 11 Q3 5 8 2"/>
    <circle cx="17.5" cy="12" r="3.8"/><path d="M14 11 Q15 5 20 2"/>
  </g>
</svg>
<div class="quote-author" style="left:210px">-Marco T.</div>
<div class="quote-author" style="left:705px">-Lena W.</div>
<div class="dots"><span class="on"></span><span></span><span></span><span></span></div>

<!-- examples -->
<h2 class="examples-title">See Real Examples from our Customers</h2>
<div class="example current" style="left:120px;top:2470px"><div class="example-img light" role="img" aria-label="Customer build: relay deck on clear standoff plates"></div><p class="example-name">Relay Deck R8-72 w/ Z16v3 +</p><p class="example-sub">Expansion board</p></div>
<div class="example" style="left:367px;top:2470px"><div class="example-img" role="img" aria-label="Customer build: controller board on black mounting plate"></div><p class="example-name">Relay Deck R8-72 w/ Z16v3 +</p><p class="example-sub">Expansion board</p></div>
<div class="example" style="left:615px;top:2470px"><div class="example-img" role="img" aria-label="Customer build: relay boards on stacked plates"></div><p class="example-name">Relay Deck R8-72 w/ Z16v3 +</p><p class="example-sub">Expansion board</p></div>
<div class="example" style="left:862px;top:2470px"><div class="example-img psu" role="img" aria-label="Customer build: power supply stacked above controller"></div><p class="example-name">Relay Deck R8-72 w/ Z16v3 +</p><p class="example-sub">Expansion board</p></div>
<div class="example" style="left:120px;top:2770px"><div class="example-img psu" role="img" aria-label="Customer build: power supply on black plate"></div><p class="example-name">Relay Deck R8-72 w/ Z16v3 +</p><p class="example-sub">Expansion board</p></div>
<div class="example" style="left:367px;top:2770px"><div class="example-img psu" role="img" aria-label="Customer build: low profile power supply kit"></div><p class="example-name">Relay Deck R8-72 w/ Z16v3 +</p><p class="example-sub">Expansion board</p></div>
<div class="example" style="left:615px;top:2770px"><div class="example-img" role="img" aria-label="Customer build: controller with fan on rounded plate"></div><p class="example-name">Relay Deck R8-72 w/ Z16v3 +</p><p class="example-sub">Expansion board</p></div>
<div class="example" style="left:862px;top:2770px"><div class="example-img" role="img" aria-label="Customer build: two boards on raised standoffs"></div><p class="example-name">Relay Deck R8-72 w/ Z16v3 +</p><p class="example-sub">Expansion board</p></div>

<footer class="site-footer">
  <p class="copyright">Copyright 2020 @ vornatic designer</p>
  <p class="follow">Follow Us:</p>
  <span class="social" style="left:998px"></span>
  <span class="social" style="left:1045px"></span>
</footer>

</body>
</html>
```